Stickers for a liquor bottle

I need 4 stickers for a liquor bottle. There shall be 3 rectangular stickers on the sides and one round sticker on top. You can be absolutely creative. Only the text and the EAN-code must be on the stickers. The rest is up to you. The alcohol is made from barley malt. There is apple, cinnamon, vanilla, caramel, honey in it.

```html
<!DOCTYPE html>
<html lang="de">
<head>
<meta charset="utf-8">
<title>Flaschenetikett – Seitenetikett Geschichte</title>
<link rel="stylesheet" href="https://fonts.googleapis.com/css2?family=Barlow+Condensed:wght@400&display=swap">
<style>
  :root {
    --label-green: #243026;
    --label-gold: #fcc419;
  }
  html, body {
    margin: 0;
    padding: 0;
    width: 1000px;
    height: 1200px;
    overflow: hidden;
    background: var(--label-green);
  }
  .label {
    position: relative;
    width: 1000px;
    height: 1200px;
    background: var(--label-green);
  }
  .label-frame {
    position: absolute;
    inset: 0;
  }
  .moon {
    position: absolute;
    left: 415px;
    top: 88px;
    width: 170px;
    height: 170px;
  }
  .story {
    position: absolute;
    left: 80px;
    right: 80px;
    top: 284px;
    margin: 0;
    font-family: "Barlow Condensed", "Arial Narrow", sans-serif;
    font-weight: 400;
    font-size: 53px;
    line-height: 78px;
    text-align: center;
    color: var(--label-gold);
  }
  .signature {
    position: absolute;
    left: 345px;
    top: 1000px;
    width: 310px;
    height: 125px;
    background: var(--label-gold);
    opacity: 0.9;
    border-radius: 6px;
  }
</style>
</head>
<body>
  <main class="label">
    <svg class="label-frame" width="1000" height="1200" viewBox="0 0 1000 1200" aria-hidden="true">
      <polygon points="82,54 918,54 953,89 953,1116 918,1151 82,1151 47,1116 47,89"
               fill="none" stroke="var(--label-gold)" stroke-width="2.5"/>
    </svg>

    <svg class="moon" viewBox="0 0 170 170" aria-hidden="true">
      <defs>
        <mask id="crescent-cut">
          <rect width="170" height="170" fill="#fff"/>
          <circle cx="108" cy="62" r="72" fill="#000"/>
        </mask>
      </defs>
      <circle cx="85" cy="85" r="80" fill="var(--label-gold)" mask="url(#crescent-cut)"/>
    </svg>

    <p class="story">
      Ich habe in meiner mikro-brauerei aus<br>
      reinem gersten- malz würze gebraut,<br>
      diese mit hefe vergoren und danach<br>
      gebrannt. Anschliessend habe ich mich<br>
      von den alten schwarzbrennern in den<br>
      usa inspirieren lassen und Das destillat<br>
      mit äpfeln, zucker, karamell, honig,<br>
      vanille, zimt und weiteren exotischen<br>
      gewürzen verfeinert.
    </p>

    <div class="signature" role="img" aria-label="Handgeschriebener Schriftzug: by Mira"></div>
  </main>
</body>
</html>
```